Business Card for Sugared Soiree

I have a logo for my candy buffet business, and need a business card designed using that logo. Sugared Soiree designs and builds beautiful and delicious candy and dessert tables for all kinds of events. The card should be simple, modern, graphic, colorful, and use the Sugared Soiree Logo.

Target Market(s)

The target market is people hosting major parties and events. This includes brides getting married, parents hosting birthday parties/Sweet Sixteen/Bar Mitzvah/quinceanera parties, and companies hosting corporate events.

Industry/Entity Type

Business

Requirements
Must have
• The business card must have the logo, with or without the tag line.

The following information must be on the card:

Dana Whitfield
CEO & Candy Stylist
614.392.5071
dana@sugaredsoiree-example.com
Nice to have
• I like the idea of having multiple colors of the same design so that several people receiving cards will each receive a different color. Perhaps 3-5 colors or variations on a basic card design.

```html
<!DOCTYPE html>
<html lang="en">
<head>
<meta charset="utf-8">
<title>Sugared Soiree – Business Card</title>
<link rel="stylesheet" href="https://fonts.googleapis.com/css2?family=Didact+Gothic&family=Open+Sans:wght@400;600&family=Advent+Pro:wght@400&display=swap">
<style>
  :root {
    --bg: #ece8e2;
    --paper: #ffffff;
    --pink: #ec1e8a;
    --green: #4cb857;
    --ink: #1d1d1f;
    --muted: #444444;
  }
  * { box-sizing: border-box; margin: 0; padding: 0; }
  html, body { width: 1200px; height: 1200px; overflow: hidden; background: var(--bg); }
  .canvas { position: relative; width: 1200px; height: 1200px; }
  .card {
    position: absolute; left: 100px; width: 1000px; height: 560px;
    background: var(--paper); overflow: hidden;
    box-shadow: 0 6px 18px rgba(0,0,0,.18);
  }
  .card--front { top: 30px; }
  .card--back { top: 615px; }
  .card__shapes { position: absolute; inset: 0; width: 1000px; height: 560px; }

  .brand-name {
    position: absolute; font-family: "Didact Gothic", sans-serif;
    color: var(--ink); font-weight: 400; line-height: 1; white-space: nowrap;
  }
  .card--front .brand-name { left: 0; right: 0; top: 215px; text-align: center; font-size: 92px; }
  .card--back .brand-name { left: 40px; top: 225px; font-size: 62px; }

  .front__web {
    position: absolute; left: 470px; top: 488px; width: 380px; text-align: center;
    font-family: "Open Sans", sans-serif; font-weight: 600; font-size: 21px; color: #fff;
  }

  .holder { position: absolute; right: 60px; top: 52px; text-align: right; }
  .holder__name { font-family: "Advent Pro", sans-serif; font-size: 40px; color: var(--ink); line-height: 1; }
  .holder__role { font-family: "Didact Gothic", sans-serif; font-size: 16px; color: var(--muted); margin-top: 8px; }

  .contacts { position: absolute; left: 44px; top: 390px; font-family: "Open Sans", sans-serif; font-size: 21px; color: var(--ink); }
  .contacts__row { display: flex; gap: 40px; margin-bottom: 10px; }
  .contact { display: flex; align-items: center; gap: 10px; }
  .contact svg { width: 22px; height: 22px; flex: none; }
</style>
</head>
<body>
<main class="canvas">

  <section class="card card--front" aria-label="Card front">
    <svg class="card__shapes" viewBox="0 0 1000 560" aria-hidden="true">
      <rect x="0" y="0" width="1000" height="30" fill="var(--pink)"/>
      <path d="M0 515 H440 V560 H0 Z" fill="var(--green)"/>
      <path d="M410 560 C430 490 450 472 510 472 H860 C890 472 900 470 910 455 V560 Z" fill="var(--pink)"/>
      <path d="M850 560 C870 470 890 440 950 432 H1000 V560 Z" fill="var(--green)"/>
    </svg>
    <div class="brand-name">Sugared Soiree</div>
    <div class="front__web">www.sugaredsoiree-example.com</div>
  </section>

  <section class="card card--back" aria-label="Card back">
    <svg class="card__shapes" viewBox="0 0 1000 560" aria-hidden="true">
      <rect x="0" y="0" width="1000" height="22" fill="var(--pink)"/>
      <path d="M0 472 H700 Q735 472 760 492 H0 Z" fill="var(--pink)"/>
      <path d="M0 490 H740 C810 490 805 375 890 372 H1000 V560 H0 Z" fill="var(--green)"/>
    </svg>

    <div class="holder">
      <div class="holder__name">Dana Whitfield</div>
      <div class="holder__role">CEO &amp; Candy Stylist</div>
    </div>

    <div class="brand-name">Sugared Soiree</div>

    <div class="contacts">
      <div class="contacts__row">
        <span class="contact">
          <svg viewBox="0 0 24 24" aria-hidden="true"><path d="M6.6 10.8a15 15 0 0 0 6.6 6.6l2.2-2.2a1 1 0 0 1 1-.25 11.4 11.4 0 0 0 3.6.57 1 1 0 0 1 1 1V20a1 1 0 0 1-1 1A17 17 0 0 1 3 4a1 1 0 0 1 1-1h3.5a1 1 0 0 1 1 1c0 1.25.2 2.450.57 3.57a1 1 0 0 1-.25 1z" fill="var(--pink)"/></svg>
          614.392.5071
        </span>
        <span class="contact">
          <svg viewBox="0 0 24 24" aria-hidden="true"><rect x="2" y="5" width="20" height="14" fill="var(--pink)"/><path d="M2 5 L12 13 L22 5" fill="none" stroke="#fff" stroke-width="1.6"/></svg>
          dana@sugaredsoiree-example.com
        </span>
      </div>
      <div class="contacts__row">
        <span class="contact">
          <svg viewBox="0 0 24 24" aria-hidden="true"><g fill="none" stroke="var(--pink)" stroke-width="1.6"><circle cx="12" cy="12" r="9.5"/><ellipse cx="12" cy="12" rx="4.2" ry="9.5"/><path d="M2.5 12h19M4 7h16M4 17h16"/></g></svg>
          www.sugaredsoiree-example.com
        </span>
      </div>
    </div>
  </section>

</main>
</body>
</html>
```